Business Card Design

Brindaro is a floral design company for weddings and special events.
Colours wanted are dark grey, aqua blue, white and black.
dark grey for the background, and the Brindaro in the aqua blue, rest of the writing in white and black etc.

Our floral design style is Rustic, textural, natural,
Wanting some kind of simplistic flower symbol next to the Brindaro see pictures.

Hi im so sorry I've changed some criteria. been confused on how this site works and what i want!! hope this is more straight forward. I also need clip art of the simple floral design i attached for my web site and also car magnets. thank you thank you thank YOU!!!! cherrs Pam

I have attached x5 ideas on where to place the lotus flower next to and around the brindaro. please use simliar colours of the flower as pictured. please cut out the white back ground from the flower. use only petals. use only lotus or the other icon provided per idea. still deciding on which one to use so waiting to see what looks best with your designs. thank you so very much in advance.!! Kindest REgards Pam

hi i am currently getting a logo design made through this also so can we wait until it is complete before any revisions are made. sorry about the delay!! thank you thank you thank you!! kind regards Pam

Reason: im having a logo made also to use on the cards. please hold off on any designs until this is received. thank you and so sorry about this!! cheers pAm

Target Market(s)

modern elegant professional

Industry/Entity Type

Floral

Contact Information for Business Card

Front:
brindaro floral design (all lower case) floral design in smaller writting)
www.brindarofloraldesign.example.au

Back:
Wedding and event design

Pamela - 0452908164
brindaro@quelnet.example.au
Rhoda-0429876513
floristrhodakessing@mailhub.example.com

Marrowin Heads, Coral Coast, QLD

Font styles to use
Other font styles liked:
• corben, cookie

Colors
87d0c7
34b8a4
eaf2ce
ffffff
e4daeb
cfdeed

Requirements
Must have
• ; dark grey for back ground. or possible all white?
;brindaro floral designs in lower case and in blue' green aqua colour. all other writing in white.
icon which i can also use on the website. see pictures(i want to use the same on my web site.. if you can please make me an clip art icon also?
Nice to have
• simple elegant, earthy, flower icon
or second option icon of lotus looking flower brindaro inside
fonts please: brindaro floral design in (corben)
all writing on the back in (cookie)
maybe have the same icon clip art provided faintly on the back, bold on the front?
i also need car magnets to

```html
<!DOCTYPE html>
<html lang="en">
<head>
<meta charset="utf-8">
<title>Brindaro Floral Design – Business Cards</title>
<link rel="stylesheet" href="https://fonts.googleapis.com/css2?family=Pinyon+Script&family=Cormorant+Garamond:wght@500&family=Cinzel:wght@400;700&display=swap">
<style>
  :root {
    --backdrop: #2f2f30;
    --card-white: #ffffff;
    --aqua: #2bb3a1;
    --aqua-dark: #1f9c8b;
    --aqua-light: #87d0c7;
    --pattern-grey: #d9dcdc;
    --pattern-grey-dark: #c3c8c8;
    --ink: #1b1b1b;
    --text-white: #ffffff;
  }
  * { margin: 0; padding: 0; box-sizing: border-box; }
  html, body {
    width: 1200px; height: 900px; overflow: hidden;
    background: var(--backdrop);
  }
  .card {
    position: absolute;
    width: 560px; height: 320px;
    background: var(--card-white);
    overflow: hidden;
    box-shadow: 0 10px 28px rgba(0,0,0,.45);
  }
  .card svg.card-art { position: absolute; inset: 0; }
  .card-front { left: 320px; top: 95px; }
  .card-back  { left: 320px; top: 485px; }

  /* Front */
  .brand-name {
    position: absolute; left: 250px; top: 96px;
    font-family: "Pinyon Script", cursive;
    font-size: 50px; color: var(--text-white); line-height: 1;
  }
  .brand-tagline {
    position: absolute; left: 258px; top: 150px;
    font-family: "Cormorant Garamond", serif; font-weight: 500;
    font-size: 42px; color: var(--text-white); line-height: 1;
  }
  .brand-web {
    position: absolute; left: 168px; top: 222px;
    font-family: "Cormorant Garamond", serif; font-weight: 500;
    font-size: 16px; letter-spacing: 1.2px; color: var(--text-white);
  }

  /* Back */
  .service-title {
    position: absolute; left: 220px; top: 8px; width: 240px;
    font-family: "Pinyon Script", cursive;
    font-size: 30px; line-height: 26px; color: var(--aqua);
    text-align: center;
  }
  .contact-person { position: absolute; font-family: "Cinzel", serif; }
  .contact-person .name { font-weight: 700; font-size: 12px; letter-spacing: 1.5px; color: var(--ink); }
  .contact-person .phone { font-size: 13px; letter-spacing: 1px; color: var(--aqua); }
  .person-rhoda { left: 58px; top: 96px; }
  .person-pamela { left: 196px; top: 122px; }

  .contact-list {
    position: absolute; left: 26px; top: 170px;
    list-style: none;
    font-family: "Cinzel", serif; font-size: 10px; letter-spacing: 0.6px;
    color: var(--text-white);
  }
  .contact-list li { display: flex; align-items: center; height: 24px; white-space: nowrap; }
  .contact-list svg { width: 13px; height: 13px; margin-right: 10px; flex: none; }
</style>
</head>
<body>

<!-- Front of card -->
<section class="card card-front">
  <svg class="card-art" viewBox="0 0 560 320" width="560" height="320">
    <defs>
      <radialGradient id="bouquetFront" cx="45%" cy="50%" r="65%">
        <stop offset="0" stop-color="#b3262c"/>
        <stop offset=".45" stop-color="#f1efe6"/>
        <stop offset=".75" stop-color="#4f7a3a"/>
        <stop offset="1" stop-color="#ffffff"/>
      </radialGradient>
    </defs>
    <rect class="pattern-band" x="90" y="262" width="470" height="58" fill="var(--pattern-grey)" role="img" aria-label="Grey floral damask pattern band"/>
    <rect class="pattern-band" x="290" y="0" width="270" height="56" fill="var(--pattern-grey)" role="img" aria-label="Grey floral damask pattern band"/>
    <path class="aqua-panel" d="M300 56 L560 56 L560 262 L112 262 C165 185 225 110 300 56 Z" fill="var(--aqua)"/>
    <path class="bouquet-photo" d="M0 20 Q150 -15 292 30 C230 90 170 160 112 262 L0 262 Z" fill="url(#bouquetFront)" role="img" aria-label="Photo of red roses and white lilies bouquet"/>
    <path class="curve-edge" d="M300 44 C225 100 165 180 104 266" fill="none" stroke="var(--card-white)" stroke-width="5"/>
    <path class="curve-edge" d="M308 46 C233 104 173 182 114 268" fill="none" stroke="var(--aqua-light)" stroke-width="1.5"/>
  </svg>
  <div class="brand-name">Brindaro</div>
  <div class="brand-tagline">Floral Design</div>
  <div class="brand-web">www.brindarofloraldesign.example.au</div>
</section>

<!-- Back of card -->
<section class="card card-back">
  <svg class="card-art" viewBox="0 0 560 320" width="560" height="320">
    <defs>
      <radialGradient id="bouquetBack" cx="50%" cy="45%" r="60%">
        <stop offset="0" stop-color="#c0272d"/>
        <stop offset=".5" stop-color="#3f8a35"/>
        <stop offset=".85" stop-color="#e8ece4"/>
        <stop offset="1" stop-color="#ffffff" stop-opacity="0"/>
      </radialGradient>
    </defs>
    <rect class="aqua-band" x="0" y="158" width="500" height="140" fill="var(--aqua)"/>
    <rect class="pattern-band" x="496" y="110" width="64" height="210" fill="var(--pattern-grey)" role="img" aria-label="Grey floral damask pattern band"/>
    <ellipse class="bouquet-photo" cx="432" cy="150" rx="60" ry="60" fill="url(#bouquetBack)" role="img" aria-label="Photo of red rose arrangement in a dark pot"/>
  </svg>

  <div class="service-title">Wedding<br>and<br>event specialists</div>

  <div class="contact-person person-rhoda">
    <div class="name">RHODA</div>
    <div class="phone">0429876513</div>
  </div>
  <div class="contact-person person-pamela">
    <div class="name">PAMELA</div>
    <div class="phone">0452908164</div>
  </div>

  <ul class="contact-list">
    <li>
      <svg viewBox="0 0 16 16" aria-hidden="true"><circle cx="8" cy="8" r="6.5" fill="none" stroke="#fff" stroke-width="1.3"/><path d="M1.5 8h13M8 1.5c-3 3.5-3 9.5 0 13M8 1.5c3 3.5 3 9.5 0 13" fill="none" stroke="#fff" stroke-width="1.1"/></svg>
      BRINDARO@QUELNET.EXAMPLE.AU
    </li>
    <li>
      <svg viewBox="0 0 16 16" aria-hidden="true"><rect x="1" y="3" width="14" height="10" fill="#fff"/><path d="M1 3l7 6 7-6" fill="none" stroke="var(--aqua)" stroke-width="1.3"/></svg>
      FLORISTRHODAKESSING@MAILHUB.EXAMPLE.COM
    </li>
    <li>
      <svg viewBox="0 0 16 16" aria-hidden="true"><path d="M8 15s5-5.5 5-9a5 5 0 0 0-10 0c0 3.5 5 9 5 9z" fill="#fff"/><circle cx="8" cy="6" r="1.8" fill="var(--aqua)"/></svg>
      MARROWIN HEADS, CORAL COAST, QLD
    </li>
  </ul>
</section>

</body>
</html>
```